Documentary Feature Film Poster

We need a poster designed for our feature documentary called Warden of Ashwater, about Liu Bo, a man who for the past 10 years, has volunteered to patrol the Huoshan River Bridge in Nanjing, China, saving the lives of those who come to throw themselves into the murky waters below.

The story follows Liu as he struggles to balance his job, his family life, and his own demons, all while taking on the responsibility to save others on the bridge.

To this day, he has saved over 250 people.

It's a very serious film, so the look should be very minimalist and sleek. Film title could have an asian feel but not cliche.. and does't have to have a Chinese look to it. You could look at Chinese stamps for inspiration on that. But we are open to anything.

I added more info to the description.

Please, note to all... The Chinese characters must have a brush stroke looking font. The boxy look is too industrial looking, and I can't paste the correct look into the instruction. There are many free, nice looking brushstroke fonts out there. Also, I was just informed that, 守望在临川 is a better title... it's just swapping the two words and changing the particle in the middle.

Hey guys, We just held a vote... and me and my partner are trying to make our decision soon. But just so you know, we will be looking for someone to design the website for the film. So, if you are also into web design, please hold on to your elements... we will be posting another pixel forge contest soon.

Requirements
Must have
• The bridge and Mr. Liu. How ever those are blended together, as long as it isn't too busy. (Boy at sea is a fantastic minimalistic poster... but ours could have a bit more going on...) maybe even two scenes separated by the text in the middle. See what works.

Muted colors... look at the posters for "slow boat north" and "past the lanfeng" to know the feeling and/or style we like.
Nice to have
• I think a play on the colors red, black, and grey will work best here... Using the sky as the backdrop for the title.

the co-directors names are Marcus T. Bellamy and Dylan Whitcombe.... they could be at the bottom. There are others involved, so you could have filler names for now.

There is a tag line from the film, that could be used "If you step back, there is always a bigger space for you." If used, I wouldn't want it so prominent. I would want it very subtle, if used at all.

And the title in chinese is 临川的守望.... you can incorporate it, it it looks nice.
Should not have
• too much going on.

```html
<!DOCTYPE html>
<html lang="en">
<head>
<meta charset="utf-8">
<title>Warden of Ashwater — Poster</title>
<link rel="stylesheet" href="https://fonts.googleapis.com/css2?family=Oswald:wght@400;700&family=Ma+Shan+Zheng&display=swap">
<style>
  :root {
    --page: #e8e6e2;
    --poster: #363636;
    --poster-dark: #2a2a2a;
    --band-grey: #8a8a8a;
    --accent-red: #7d1515;
    --title-red: #b3191c;
    --ink-white: #f2f2f2;
    --ink-soft: #bdbdbd;
    --outline: #0d0d0d;
  }
  * { margin: 0; padding: 0; box-sizing: border-box; }
  html, body {
    width: 1200px;
    height: 1148px;
    overflow: hidden;
    background: var(--page);
  }
  .poster {
    position: absolute;
    left: 230px;
    top: 24px;
    width: 740px;
    height: 1100px;
    background: var(--poster);
    overflow: hidden;
    box-shadow: 0 10px 30px rgba(0,0,0,0.25);
  }
  .poster-shapes {
    position: absolute;
    inset: 0;
    width: 740px;
    height: 1100px;
  }
  .title-block {
    position: absolute;
    left: 0;
    right: 0;
    top: 640px;
    text-align: center;
  }
  .film-title {
    font-family: "Oswald", sans-serif;
    font-weight: 700;
    font-size: 78px;
    line-height: 1;
    letter-spacing: 4px;
    text-transform: uppercase;
    color: var(--ink-white);
    -webkit-text-stroke: 2px var(--outline);
    text-shadow: 0 0 1px var(--ink-white);
  }
  .film-title .title-joiner {
    font-size: 34px;
    letter-spacing: 1px;
    vertical-align: baseline;
  }
  .film-title .title-initial { color: var(--title-red); }
  .tagline {
    margin-top: 10px;
    font-family: "Oswald", sans-serif;
    font-weight: 700;
    font-size: 13px;
    letter-spacing: 5.5px;
    text-transform: uppercase;
    color: var(--ink-white);
  }
  .chinese-title {
    margin-top: 8px;
    font-family: "Ma Shan Zheng", cursive;
    font-size: 66px;
    line-height: 1.1;
    letter-spacing: 10px;
    color: var(--title-red);
  }
  .directors {
    margin-top: 6px;
    font-family: "Oswald", sans-serif;
    font-weight: 700;
    font-size: 24px;
    letter-spacing: 1.5px;
    text-transform: uppercase;
    color: var(--ink-white);
  }
  .credits {
    width: 590px;
    margin: 8px auto 0;
    font-family: "Oswald", sans-serif;
    font-weight: 400;
    font-size: 10px;
    line-height: 1.45;
    letter-spacing: 0.6px;
    text-transform: uppercase;
    text-align: left;
    color: var(--ink-soft);
  }
  .still-strip {
    position: absolute;
    left: 30px;
    right: 30px;
    top: 985px;
    height: 78px;
    display: flex;
    gap: 4px;
  }
  .still {
    flex: 1;
    background: linear-gradient(180deg, #9a9a9a, #2b2b2b);
  }
  .still.wide { flex: 1.3; }
  .still.light { background: linear-gradient(180deg, #d4d4d4, #6f6f6f); }
</style>
</head>
<body>
  <main class="poster">
    <svg class="poster-shapes" viewBox="0 0 740 1100" aria-hidden="false">
      <rect class="top-band" x="0" y="0" width="740" height="1100" fill="var(--poster)"/>
      <rect class="header-band" x="0" y="0" width="740" height="100" fill="var(--poster-dark)"/>
      <polygon class="header-red-stripe" points="12,104 728,84 728,100 12,120" fill="var(--accent-red)"/>
      <polygon class="header-grey-stripe" points="12,120 728,100 728,112 12,132" fill="var(--band-grey)"/>
      <polygon class="bridge-scene" role="img"
        aria-label="Black and white photograph: a man in silhouette looking out over the misty Huoshan River Bridge, lamp posts and a bus fading into fog"
        points="12,138 728,118 728,478 12,578"
        fill="url(#sceneTone)"/>
      <polygon class="divider-grey" points="12,578 728,478 728,500 12,600" fill="var(--band-grey)"/>
      <polygon class="divider-red" points="12,600 728,500 728,522 12,622" fill="var(--accent-red)"/>
      <defs>
        <linearGradient id="sceneTone" x1="0" y1="0" x2="1" y2="0.4">
          <stop offset="0" stop-color="#a9a9a9"/>
          <stop offset="0.45" stop-color="#dcdcdc"/>
          <stop offset="0.75" stop-color="#5a5a5a"/>
          <stop offset="1" stop-color="#1e1e1e"/>
        </linearGradient>
      </defs>
    </svg>

    <section class="title-block">
      <h1 class="film-title">Warden<span class="title-joiner">of</span><span class="title-initial">A</span>shwater</h1>
      <p class="tagline">If you step back, there is always a bigger space for you</p>
      <p class="chinese-title" lang="zh">临川的守望</p>
      <p class="directors">Marcus T. Bellamy and Dylan Whitcombe</p>
      <p class="credits">Produced with care by Nora Vance, edited by Elias Grant, music by Tomas Reyes, photography by Ivy Hale, sound by Omar Feld, executive producers Ruth Allen and Sam Ortiz, associate producer Lena Marsh, coloring by Petra Lund, a documentary about one bridge, one man, and the quiet courage of waiting.</p>
    </section>

    <section class="still-strip">
      <div class="still" role="img" aria-label="Film still: Mr. Liu in sunglasses beside parked cars"></div>
      <div class="still light" role="img" aria-label="Film still: roadside on the bridge approach"></div>
      <div class="still wide" role="img" aria-label="Film still: close view of Mr. Liu wearing sunglasses"></div>
      <div class="still light" role="img" aria-label="Film still: the bridge towers in haze"></div>
      <div class="still" role="img" aria-label="Film still: Mr. Liu in a cap at dusk"></div>
    </section>
  </main>
</body>
</html>
```